International school needs an amazing design for our character traits!

We are the Northbridge School of Calvera and promote character traits using an acronym of our school mascot, the LANTERN.
Fearless
Aware
Leaders
Curious
Open-minded
Noble
Self-motivated

Right now, these are only words on a page that we try to bring to life. It would be great to have a visual to go with the words - to promote the image of what we are looking for.

Target Market(s)

Students and Families

Industry/Entity Type

Education

Font styles to use
Sans Serif

Colors

Designer to choose colors to be used in the design.

Requirements
Must have
• Images

```html
<!DOCTYPE html>
<html lang="en">
<head>
<meta charset="utf-8">
<title>Northbridge School of Calvera – LANTERN Character Traits</title>
<link href="https://fonts.googleapis.com/css2?family=Ubuntu:wght@400;500&display=swap" rel="stylesheet">
<style>
  :root {
    --sky-top: #2fa6c8;
    --sky-mid: #a9d6df;
    --haze: #efe9dc;
    --sunset: #f3b264;
    --ridge: #8a4e2c;
    --white: #ffffff;
    --pill-tab: #f1f1f1;
    --number: #a9a9a9;
    --navy: #0b4aa2;
    --fearless: #e30613;
    --aware: #5cb82a;
    --leaders: #dfa600;
    --curious: #3a9fe6;
    --open: #c026d3;
    --noble: #5417d4;
    --motivated: #8b3f12;
    --frame: #f4f6f6;
    --frame-blue: #a6d8e6;
  }
  * { box-sizing: border-box; margin: 0; padding: 0; }
  html, body { width: 1200px; height: 927px; overflow: hidden; }
  body { font-family: "Ubuntu", sans-serif; background: var(--white); }
  .canvas { position: relative; width: 1200px; height: 927px; overflow: hidden; }
  .backdrop {
    position: absolute; inset: 0;
    background:
      radial-gradient(ellipse 520px 220px at 700px 927px, rgba(255,200,120,.85), rgba(255,200,120,0) 70%),
      linear-gradient(180deg, var(--sky-top) 0%, var(--sky-mid) 30%, var(--haze) 60%, #f6d9ad 85%, var(--sunset) 100%);
  }
  .ridge {
    position: absolute; left: 0; right: 0; bottom: 0; height: 160px;
    background: linear-gradient(180deg, rgba(138,78,44,0) 0%, rgba(180,100,50,.55) 60%, var(--ridge) 100%);
    clip-path: polygon(0 100%, 25% 92%, 45% 70%, 60% 45%, 75% 30%, 88% 22%, 100% 15%, 100% 100%);
  }
  .figure-zone {
    position: absolute; left: 905px; top: 275px; width: 230px; height: 410px;
    background: radial-gradient(ellipse at center, rgba(110,70,50,.28), rgba(110,70,50,0) 70%);
  }
  .graphics { position: absolute; inset: 0; }
  .school-name {
    position: absolute; left: 147px; top: 400px; width: 280px;
    text-align: center; font-weight: 500; font-size: 30px; line-height: 1.15;
    color: var(--navy);
  }
  .trait { position: absolute; height: 73px; }
  .trait-pill {
    position: absolute; inset: 0;
    background: var(--white);
    border-radius: 0 37px 37px 0;
    box-shadow: 0 4px 8px rgba(0,0,0,.12);
    overflow: hidden;
  }
  .trait-pill::before {
    content: ""; position: absolute; right: 0; top: 0; bottom: 0; width: 72px;
    background: var(--pill-tab);
    clip-path: polygon(14px 0, 100% 0, 100% 100%, 0 100%);
  }
  .trait-pill::after {
    content: ""; position: absolute; inset: 3px 3px 3px 0;
    border: 1px dashed var(--accent);
    border-left: none;
    border-radius: 0 34px 34px 0;
  }
  .trait-name {
    position: absolute; left: 27px; top: 0; line-height: 73px;
    font-size: 24px; color: var(--accent);
  }
  .trait-number {
    position: absolute; right: 24px; top: 0; line-height: 73px;
    font-size: 24px; color: var(--number);
  }
  .fearless { --accent: var(--fearless); left: 560px; top: 63px; width: 264px; }
  .aware { --accent: var(--aware); left: 676px; top: 173px; width: 265px; }
  .leaders { --accent: var(--leaders); left: 742px; top: 288px; width: 262px; }
  .curious { --accent: var(--curious); left: 764px; top: 429px; width: 261px; }
  .open { --accent: var(--open); left: 742px; top: 569px; width: 261px; }
  .noble { --accent: var(--noble); left: 676px; top: 684px; width: 265px; }
  .motivated { --accent: var(--motivated); left: 555px; top: 792px; width: 264px; }
  .trait.curious .trait-name, .trait.open .trait-name { left: 28px; }
</style>
</head>
<body>
<main class="canvas">
  <div class="backdrop" role="img" aria-label="Photo of a bright blue sky fading into a warm sunset over a mountain ridge"></div>
  <div class="ridge"></div>
  <div class="figure-zone" role="img" aria-label="Silhouette of a child jumping with arms raised against the sky"></div>

  <svg class="graphics" width="1200" height="927" viewBox="0 0 1200 927">
    <!-- emblem frame -->
    <circle cx="287" cy="457" r="209" fill="var(--frame)" opacity=".75"/>
    <circle cx="287" cy="457" r="188" fill="var(--frame-blue)"/>
    <circle cx="287" cy="457" r="180" fill="#c6e6ee"/>
    <circle cx="287" cy="457" r="167" fill="#e3f3f6"/>
    <circle cx="287" cy="457" r="150" fill="var(--white)"/>

    <!-- connector arc -->
    <g fill="none" stroke-width="1.6">
      <path d="M287 219 A238 238 0 0 1 391 243" stroke="var(--white)"/>
      <path d="M391 243 A238 238 0 0 1 464 299" stroke="var(--fearless)"/>
      <path d="M464 299 A238 238 0 0 1 510 377" stroke="var(--aware)"/>
      <path d="M510 377 A238 238 0 0 1 523 457" stroke="var(--leaders)"/>
      <path d="M523 457 A238 238 0 0 1 510 536" stroke="var(--curious)"/>
      <path d="M510 536 A238 238 0 0 1 462 615" stroke="var(--open)"/>
      <path d="M462 615 A238 238 0 0 1 391 669" stroke="var(--noble)"/>
      <path d="M391 669 A238 238 0 0 1 287 695" stroke="var(--motivated)"/>
    </g>

    <!-- spokes to icons -->
    <g stroke-width="1">
      <line x1="391" y1="243" x2="493" y2="126" stroke="var(--fearless)"/>
      <line x1="464" y1="299" x2="596" y2="222" stroke="var(--aware)"/>
      <line x1="510" y1="377" x2="655" y2="330" stroke="var(--leaders)"/>
      <line x1="523" y1="457" x2="675" y2="457" stroke="var(--curious)"/>
      <line x1="510" y1="536" x2="654" y2="582" stroke="var(--open)"/>
      <line x1="462" y1="615" x2="594" y2="690" stroke="var(--noble)"/>
      <line x1="391" y1="669" x2="490" y2="784" stroke="var(--motivated)"/>
    </g>

    <!-- arc dots -->
    <g stroke="var(--white)" stroke-width="4">
      <circle cx="391" cy="243" r="13" fill="var(--fearless)"/>
      <circle cx="464" cy="299" r="13" fill="var(--aware)"/>
      <circle cx="510" cy="377" r="13" fill="var(--leaders)"/>
      <circle cx="523" cy="457" r="13" fill="var(--curious)"/>
      <circle cx="510" cy="536" r="13" fill="var(--open)"/>
      <circle cx="462" cy="615" r="13" fill="var(--noble)"/>
      <circle cx="391" cy="669" r="13" fill="var(--motivated)"/>
    </g>
  </svg>

  <p class="school-name">Northbridge School of Calvera</p>

  <section class="trait fearless">
    <div class="trait-pill"><span class="trait-name">Fearless</span><span class="trait-number">01</span></div>
  </section>
  <section class="trait aware">
    <div class="trait-pill"><span class="trait-name">Aware</span><span class="trait-number">02</span></div>
  </section>
  <section class="trait leaders">
    <div class="trait-pill"><span class="trait-name">Leaders</span><span class="trait-number">03</span></div>
  </section>
  <section class="trait curious">
    <div class="trait-pill"><span class="trait-name">Curious</span><span class="trait-number">04</span></div>
  </section>
  <section class="trait open">
    <div class="trait-pill"><span class="trait-name">Open-Minded</span><span class="trait-number">05</span></div>
  </section>
  <section class="trait noble">
    <div class="trait-pill"><span class="trait-name">Noble</span><span class="trait-number">06</span></div>
  </section>
  <section class="trait motivated">
    <div class="trait-pill"><span class="trait-name">Self-Motivated</span><span class="trait-number">07</span></div>
  </section>

  <!-- trait icon badges -->
  <svg class="graphics" width="1200" height="927" viewBox="0 0 1200 927">
    <g filter="none">
      <g class="badge">
        <circle cx="515" cy="91" r="44" fill="var(--white)" stroke="var(--fearless)" stroke-width="3"/>
        <circle cx="515" cy="91" r="30" fill="#7a2a3a" role="img" aria-label="Illustration of a round red and navy hero shield with a white star"/>
      </g>
      <g class="badge">
        <circle cx="632" cy="202" r="44" fill="var(--white)" stroke="var(--aware)" stroke-width="3"/>
        <circle cx="632" cy="202" r="30" fill="#9be33a" role="img" aria-label="Illustration of a glowing green light bulb"/>
      </g>
      <g class="badge">
        <circle cx="697" cy="318" r="44" fill="var(--white)" stroke="var(--leaders)" stroke-width="3"/>
        <circle cx="697" cy="318" r="30" fill="#d9a23a" role="img" aria-label="Illustration of a golden trophy cup with a red ribbon"/>
      </g>
      <g class="badge">
        <circle cx="718" cy="457" r="44" fill="var(--white)" stroke="var(--curious)" stroke-width="3"/>
        <circle cx="718" cy="457" r="30" fill="#cfe8e6" role="img" aria-label="Illustration of colourful question marks"/>
      </g>
      <g class="badge">
        <circle cx="695" cy="597" r="44" fill="var(--white)" stroke="var(--open)" stroke-width="3"/>
        <circle cx="695" cy="597" r="30" fill="#c7a0c8" role="img" aria-label="Illustration of a rocket launching among gears"/>
      </g>
      <g class="badge">
        <circle cx="632" cy="712" r="44" fill="var(--white)" stroke="var(--noble)" stroke-width="3"/>
        <circle cx="632" cy="712" r="30" fill="#8a63e6" role="img" aria-label="Illustration of a purple crown"/>
      </g>
      <g class="badge">
        <circle cx="510" cy="821" r="44" fill="var(--white)" stroke="var(--motivated)" stroke-width="3"/>
        <circle cx="510" cy="821" r="30" fill="#e07a2a" role="img" aria-label="Illustration of an orange thought cloud with an upward arrow"/>
      </g>
    </g>
  </svg>
</main>
</body>
</html>
```